For Sale and For Rent Signs

We are a real estate agency looking for "For Sale" and "For Rent" lawn signs. I attached a copy of our logo for a point of reference. The size of the signs are 18x24. On the "For Rent" sign, I'd like to keep it simple with just our logo and number. On the "For Sale" sign, I'd like to get creative and use our initials as opposed to our logo (The name of our company has the word "rent" in it so it gets confusing when people are looking at it when the house is for sale). I'm open to different variations of our initials, such as "LMR" or "LM" with "Realty" next to it or underneath it. I also attached some sample signs that are in the ballpark of what we're looking for, and also our business card (but the sign shouldn't be modeled exactly after it). Please contact me with any questions.
Thanks!
Company Name: LarkMoor Realty
Company Phone Number: 401-586-4173
Real Estate

```html
<!DOCTYPE html>
<html lang="en">
<head>
<meta charset="utf-8">
<title>LarkMoor Realty – Lawn Signs</title>
<link rel="stylesheet" href="https://fonts.googleapis.com/css2?family=Montserrat:wght@400;500;600;700&display=swap">
<style>
  :root{
    --page:#ffffff;
    --charcoal:#3a3a3b;
    --charcoal-deep:#232324;
    --charcoal-light:#5a5a5b;
    --ink:#4a4a4b;
    --paper:#ffffff;
    --paper-shade:#e6e6e6;
    --ribbon:#b3161b;
    --ribbon-dark:#7d0c10;
    --accent:#d2231e;
    --label:#333333;
  }
  *{box-sizing:border-box;margin:0;padding:0}
  html,body{width:768px;height:1200px;overflow:hidden;background:var(--page)}
  body{position:relative;font-family:"Montserrat",Arial,sans-serif}
  .side-label{position:absolute;left:8px;font-size:20px;color:var(--label);font-weight:400}
  .side-label--one{top:20px}
  .side-label--two{top:604px}
  .sign{position:absolute;left:64px;width:640px;height:524px;overflow:hidden}
  .sign--rent{top:60px;background:var(--charcoal)}
  .sign--sale{top:640px;background:radial-gradient(ellipse at 40% 40%,var(--charcoal-light),var(--charcoal-deep) 75%)}
  .sign__shapes{position:absolute;inset:0;width:100%;height:100%}
  .ribbon{position:absolute;left:22px;width:300px;height:100px;overflow:visible}
  .ribbon__text{font-family:"Montserrat",Arial,sans-serif;font-size:30px;letter-spacing:1px;fill:#fff;font-weight:400}
  .ribbon__text tspan{font-weight:700}
  .sign--rent .ribbon{top:30px}
  .sign--sale .ribbon{top:42px}
  .brand{position:absolute;font-weight:500;line-height:1}
  .brand__name{display:block;font-size:86px;letter-spacing:-3px}
  .brand__sub{display:block;text-align:right;font-size:50px;letter-spacing:6px;margin-top:6px}
  .sign--rent .brand{left:92px;top:150px;color:var(--ink)}
  .sign--sale .brand{left:70px;top:170px;color:var(--paper)}
  .sign--sale .brand__name{font-size:150px;letter-spacing:-4px}
  .sign--sale .brand__sub{font-size:46px;margin-top:2px}
  .phone{position:absolute;font-weight:700;letter-spacing:3px;white-space:nowrap}
  .sign--rent .phone{left:0;right:0;top:440px;text-align:center;font-size:48px;color:var(--paper)}
  .sign--sale .phone{right:30px;top:448px;font-size:46px;color:var(--charcoal-deep)}
  .phone__dash{color:var(--accent)}
  .badges{position:absolute;right:34px;top:398px;display:flex;gap:10px}
  .badge{width:34px;height:30px;background:var(--charcoal-deep)}
  .badge--wide{width:50px}
</style>
</head>
<body>
  <div class="side-label side-label--one">side1</div>

  <section class="sign sign--rent">
    <svg class="sign__shapes" viewBox="0 0 640 524" aria-hidden="true">
      <path d="M0 0H640V372C560 340 470 330 380 372C280 418 150 440 0 428Z" fill="var(--paper)"/>
      <path d="M0 300C140 330 260 300 380 330C470 350 560 320 640 300V372C560 340 470 330 380 372C280 418 150 440 0 428Z" fill="var(--paper-shade)" opacity=".6"/>
    </svg>
    <svg class="ribbon" viewBox="0 0 300 100" aria-hidden="true">
      <path d="M0 66L26 46L22 92Z" fill="var(--ribbon-dark)"/>
      <path d="M18 40L282 8L296 54L26 88Z" fill="var(--ribbon)"/>
      <text class="ribbon__text" x="46" y="74" transform="rotate(-7 46 74)">FOR <tspan>RENT</tspan></text>
    </svg>
    <div class="brand">
      <span class="brand__name">LarkMoor</span>
      <span class="brand__sub">Realty</span>
    </div>
    <div class="phone">401-586-4173</div>
  </section>

  <div class="side-label side-label--two">side 2</div>

  <section class="sign sign--sale">
    <svg class="sign__shapes" viewBox="0 0 640 524" aria-hidden="true">
      <path d="M0 0H640V40C520 70 400 20 260 50C160 70 70 60 0 40Z" fill="var(--charcoal-deep)"/>
      <path d="M0 430C120 400 240 440 380 410C480 390 570 372 640 380V524H0Z" fill="var(--paper)"/>
    </svg>
    <svg class="ribbon" viewBox="0 0 300 100" aria-hidden="true">
      <path d="M0 66L26 46L22 92Z" fill="var(--ribbon-dark)"/>
      <path d="M18 40L282 8L296 54L26 88Z" fill="var(--ribbon)"/>
      <text class="ribbon__text" x="46" y="74" transform="rotate(-7 46 74)">FOR <tspan>SALE</tspan></text>
    </svg>
    <div class="brand">
      <span class="brand__name">LM</span>
      <span class="brand__sub">Realty</span>
    </div>
    <div class="badges">
      <span class="badge" aria-label="Listing badge"></span>
      <span class="badge badge--wide" aria-label="Listing service badge"></span>
      <span class="badge" aria-label="Housing badge"></span>
    </div>
    <div class="phone">401<span class="phone__dash">-</span>586<span class="phone__dash">-</span>4173</div>
  </section>
</body>
</html>
```